Wordpress website design for Pelix Bridge-Africa

We need a website for a new consultancy and digital marketplace in Kenya called 'Pelix Bridge - Africa'. Please refer to the the attached document [Pelix Bridge Africa website brief] and contact me anytime.

Bests,
Rosalind
Updates

Deadline extended to allow for additional revisions and refinements, ensuring that final designs align closely with project objectives and quality standards. This extra time will help incorporate valuable feedback and ensure the final output meets our high expectations.

Coding

```html
<!DOCTYPE html>
<html lang="en">
<head>
<meta charset="utf-8">
<title>Pelix Bridge Africa</title>
<link href="https://fonts.googleapis.com/css2?family=Playfair+Display:wght@700&family=Poppins:wght@400;500;600;700;800&display=swap" rel="stylesheet">
<style>
:root{
  --green:#12dc0c;
  --navy:#1c2152;
  --navy-deep:#15183f;
  --ink:#1b2250;
  --text:#2b2b35;
  --muted:#f4f3f5;
  --white:#ffffff;
}
*{margin:0;padding:0;box-sizing:border-box}
html,body{width:1200px;height:3550px;overflow:hidden}
body{font-family:'Poppins',sans-serif;color:var(--text);background:var(--white);position:relative}
.abs{position:absolute}
.section{position:absolute;left:0;width:1200px}
.logo{font-family:'Playfair Display',serif;font-weight:700;color:var(--white);font-size:36px;letter-spacing:.3px}
/* hero */
.hero{top:0;height:649px;background:linear-gradient(100deg,#2c3e60 0%,#4d6482 35%,#7c8ea6 60%,#3a4a66 100%)}
.hero-photo{inset:0}
.hero-shade{inset:0;background:linear-gradient(90deg,rgba(22,35,70,.75) 0%,rgba(22,35,70,.35) 55%,rgba(22,35,70,.1) 100%)}
.nav a{position:absolute;top:36px;color:var(--white);font-size:16px;text-decoration:none;font-weight:400}
.nav .active{background:var(--green);padding:2px 10px;top:32px}
.cart-badge{width:15px;height:15px;border-radius:50%;background:var(--green);color:var(--navy);font-size:9px;text-align:center;line-height:15px;font-weight:600}
.hero h1{left:154px;top:190px;width:560px;font-size:51px;line-height:58px;font-weight:700;color:var(--white)}
.btn-start{left:161px;top:456px;width:189px;height:51px;background:var(--green);color:var(--navy);font-weight:700;font-size:16px;display:flex;align-items:center;justify-content:center;gap:14px}
.dots{left:555px;top:590px;display:flex;gap:9px}
.dots span{width:11px;height:11px;border-radius:50%;border:1.5px solid var(--white)}
.dots .on{background:var(--green);border-color:var(--green)}
/* welcome */
.welcome{top:649px;height:588px;background:var(--white)}
.welcome h2{left:613px;top:68px;color:var(--ink);font-weight:800;line-height:1.15}
.welcome h2 .small{font-size:30px;display:block}
.welcome h2 .big{font-size:37px;display:block}
.rule{height:3px;background:var(--ink)}
.welcome .copy{left:726px;top:192px;width:410px;font-size:13px;line-height:21px;color:var(--text)}
.welcome .copy p{margin-bottom:19px}
/* services */
.services{top:1237px;height:569px;background:linear-gradient(135deg,#1d225a 0%,#161a46 60%,#1f2560 100%)}
.sec-title{width:100%;text-align:center;font-weight:800;font-size:34px;color:var(--ink)}
.services .sec-title{color:var(--white);top:50px}
.card{top:171px;width:273px;height:345px;background:var(--white);text-align:center}
.card.featured{background:var(--green)}
.card .icon{position:absolute;left:106px;top:42px;width:60px;height:60px}
.card h3{position:absolute;left:0;right:0;top:132px;font-size:16px;font-weight:600;color:var(--ink);line-height:22px;padding:0 14px}
.card p{position:absolute;left:24px;right:24px;top:175px;font-size:12.5px;line-height:16.5px;color:#333}
.card .btn{position:absolute;left:50%;transform:translateX(-50%);top:287px;height:30px;padding:0 16px;font-size:12px;font-weight:600;line-height:30px;background:var(--green);color:var(--white)}
.card.featured .btn{background:var(--navy-deep)}
/* categories */
.categories{top:1806px;height:685px;background:var(--white)}
.cat-img{top:182px;width:377px;height:377px}
.cat-label{top:587px;width:377px;text-align:center;font-weight:600;font-size:17px;color:var(--ink);letter-spacing:.5px}
.cat-line{top:626px;width:50px;height:2px;background:var(--green)}
/* featured */
.featured-products{top:2491px;height:740px;background:var(--muted)}
.product{top:179px;width:270px;height:451px;background:var(--white);text-align:center}
.product .thumb{position:absolute;left:0;top:0;width:270px;height:222px}
.cart-dot{position:absolute;right:12px;top:12px;width:30px;height:30px;border-radius:50%;background:var(--navy)}
.product h4{position:absolute;left:14px;right:14px;top:248px;font-size:13.5px;line-height:19px;font-weight:600;color:#111}
.product p{position:absolute;left:20px;right:20px;top:294px;font-size:11.5px;line-height:16px;color:#333}
.product .price{position:absolute;left:0;right:0;top:336px;font-size:18px;font-weight:500;color:#111}
.product .btn{position:absolute;left:50%;transform:translateX(-50%);top:388px;height:30px;padding:0 18px;line-height:30px;font-size:12px;font-weight:600;background:var(--green);color:var(--white)}
.pager{top:683px;left:520px;display:flex;align-items:center;gap:10px}
.pager i{display:block;width:10px;height:10px;border-radius:50%;background:var(--navy)}
.pager i.on{background:var(--green)}
/* footer */
.footer{top:3231px;height:319px;background:var(--navy);color:var(--white)}
.footer h5{font-size:15px;font-weight:700;letter-spacing:.3px}
.footer ul{list-style:none;font-size:12.5px;line-height:21px}
.social{display:flex;gap:8px;font-size:10px}
.social span{border:1.5px solid var(--white);border-radius:14px;padding:3px 7px}
.field{left:792px;top:87px;width:259px;height:40px;background:var(--white);color:#444;font-size:12.5px;display:flex;align-items:center;padding-left:14px;gap:10px}
.subscribe{left:792px;top:141px;width:259px;height:40px;background:var(--green);color:var(--navy);font-weight:700;font-size:15px;text-align:center;line-height:40px}
.divider{left:149px;top:224px;width:902px;height:1px;background:rgba(255,255,255,.2)}
.pay{left:150px;top:259px;display:flex;gap:10px;align-items:center;font-size:13px;font-weight:600}
.pay .chip{background:var(--white);color:var(--navy);padding:2px 6px;font-size:11px}
.copyright{left:832px;top:265px;font-size:12px}
</style>
</head>
<body>

<header class="section hero">
  <div class="abs hero-photo" role="img" aria-label="Businessman in a suit using a laptop in a bright city office"></div>
  <div class="abs hero-shade"></div>
  <div class="abs logo" style="left:154px;top:30px">Pelix Bridge</div>
  <nav class="nav">
    <a class="active" style="left:548px">Home</a>
    <a style="left:640px">Services</a>
    <a style="left:742px">Marketplace</a>
    <a style="left:876px">About Us</a>
    <a style="left:986px">Contact</a>
  </nav>
  <svg class="abs" style="left:1070px;top:36px" width="22" height="20" viewBox="0 0 22 20" fill="none" stroke="#fff" stroke-width="1.8"><path d="M1 2h4l3 11h11l2-8H6"/><circle cx="9" cy="17" r="1.5"/><circle cx="18" cy="17" r="1.5"/></svg>
  <div class="abs cart-badge" style="left:1084px;top:28px">0</div>
  <h1 class="abs">Empowering Innovations &amp; Digital Transformation Across Africa</h1>
  <div class="abs btn-start">Get Started
    <svg width="28" height="14" viewBox="0 0 28 14" fill="none" stroke="#1c2152" stroke-width="2.2"><path d="M0 7h26M20 1l6 6-6 6"/></svg>
  </div>
  <div class="abs dots"><span class="on"></span><span></span><span></span><span></span><span></span></div>
</header>

<section class="section welcome">
  <div class="abs" style="left:0;top:310px;width:150px;height:150px;background:linear-gradient(135deg,#6b6e72,#3a3d42)" role="img" aria-label="Office interior"></div>
  <div class="abs" style="left:82px;top:305px;width:200px;height:228px;background:linear-gradient(135deg,#4b4e52,#25272b)"></div>
  <div class="abs" style="left:148px;top:247px;width:175px;height:80px;background:linear-gradient(135deg,#a9adb3,#6f7379)"></div>
  <div class="abs" style="left:300px;top:61px;width:271px;height:80px;background:linear-gradient(135deg,#b8bec6,#8a9099)"></div>
  <div class="abs" style="left:300px;top:130px;width:357px;height:354px;background:linear-gradient(135deg,#c4c7ca 0%,#6b6f63 45%,#3f4b34 100%)" role="img" aria-label="Two smiling colleagues looking at a tablet together in an office"></div>
  <div class="abs" style="left:657px;top:361px;width:36px;height:30px;background:#222"></div>
  <h2 class="abs"><span class="small">WELCOME TO</span><span class="big">PELIX BRIDGE</span></h2>
  <div class="abs rule" style="left:619px;top:174px;width:40px"></div>
  <div class="abs copy">
    <p>Pelix Bridge Africa is a consultancy firm and digital marketplace dedicated to supporting Africa's digital transformation. We provide data-driven insights, strategic guidance, customised solutions to empower public and private sectors.</p>
    <p>We aim to tackle complex challenges, optimize operations, and unlock growth through innovative technology.</p>
    <p>Our marketplace offers a curated selection of digital products and tools designed to support strategic growth, expand knowledge, strengthen data capabilities, and streamline operations. With deep expertise in digital transformation and a focus on Africa's unique opportunities, Pelix Bridge Africa is your trusted partner in navigating today's dynamic digital landscape.</p>
    <p>Together, we're advancing Africa's digital future.</p>
  </div>
</section>

<section class="section services">
  <h2 class="abs sec-title">OUR SERVICES</h2>
  <div class="abs rule" style="left:582px;top:117px;width:40px;background:#fff"></div>

  <div class="abs card featured" style="left:26px">
    <svg class="icon" viewBox="0 0 60 60" fill="none" stroke="#1c2152" stroke-width="2.4"><rect x="8" y="22" width="26" height="18" rx="3"/><path d="M34 26l14-8v26l-14-8"/><circle cx="46" cy="12" r="6"/><path d="M14 40v12h8V40"/></svg>
    <h3>Digital Strategy</h3>
    <p>Lorem ipsum dolor sit amet, cons ectetur adipiscing elit, sed do eiusmod tempor incid idunt ut labore et dolore magna aliqua laboris nisi ut aliquip ex ea commod lorem ipsum.</p>
    <div class="btn">Read More</div>
  </div>
  <div class="abs card" style="left:318px">
    <svg class="icon" viewBox="0 0 60 60" fill="none" stroke="#1c2152" stroke-width="2.4"><circle cx="24" cy="18" r="9" fill="#12dc0c"/><path d="M12 18a12 12 0 0 1 24 0"/><rect x="8" y="32" width="32" height="18" rx="9"/><rect x="36" y="36" width="18" height="14" rx="2"/><circle cx="45" cy="43" r="2.5"/></svg>
    <h3>Technical Expertise</h3>
    <p>Lorem ipsum dolor sit amet, cons ectetur adipiscing elit, sed do eiusmod tempor incid idunt ut labore et dolore magna aliqua laboris nisi ut aliquip ex ea commod lorem ipsum.</p>
    <div class="btn">Read More</div>
  </div>
  <div class="abs card" style="left:612px">
    <svg class="icon" viewBox="0 0 60 60" fill="none" stroke="#1c2152" stroke-width="2.4"><rect x="6" y="8" width="48" height="34" rx="2"/><path d="M24 42v8h12v-8M18 50h24"/><path d="M30 34V24M37 34V18M44 34V21"/><circle cx="20" cy="32" r="6" fill="#12dc0c"/></svg>
    <h3>Data Analytics</h3>
    <p>Lorem ipsum dolor sit amet, cons ectetur adipiscing elit, sed do eiusmod tempor incid idunt ut labore et dolore magna aliqua laboris nisi ut aliquip ex ea commod lorem ipsum.</p>
    <div class="btn">Read More</div>
  </div>
  <div class="abs card" style="left:904px">
    <svg class="icon" viewBox="0 0 60 60" fill="none" stroke="#1c2152" stroke-width="2.4"><rect x="16" y="16" width="28" height="28" rx="2"/><rect x="22" y="22" width="16" height="16" fill="#12dc0c"/><path d="M22 4v12M30 4v12M38 4v12M22 44v12M30 44v12M38 44v12M4 22h12M4 30h12M4 38h12M44 22h12M44 30h12M44 38h12"/></svg>
    <h3>Artificial Intelligence (AI) &amp; Machine Learning (ML)</h3>
    <p style="top:190px">Lorem ipsum dolor sit amet, consectetur adipiscing elit, sed do eiusmod tempor incid id unt ut labore et</p>
    <div class="btn">Read More</div>
  </div>
</section>

<section class="section categories">
  <h2 class="abs sec-title" style="top:54px">PRODUCT CATEGORIES</h2>
  <div class="abs rule" style="left:580px;top:126px;width:40px"></div>

  <div class="abs cat-img" style="left:21px;background:linear-gradient(135deg,#e9e9ea,#bdbdbe)" role="img" aria-label="Digital magazine template spreads"></div>
  <div class="abs cat-img" style="left:415px;background:linear-gradient(135deg,#eef0f1,#cfd4d8 60%,#e8a83a)" role="img" aria-label="Colour swatches and printed guide samples on a table"></div>
  <div class="abs cat-img" style="left:806px;background:linear-gradient(135deg,#f7c91d,#f1b90a)" role="img" aria-label="Hands typing on a laptop with online course icons on a yellow background"></div>

  <div class="abs cat-label" style="left:21px">TEMPLATES</div>
  <div class="abs cat-label" style="left:415px">GUIDES</div>
  <div class="abs cat-label" style="left:806px">COURSES</div>
  <div class="abs cat-line" style="left:185px"></div>
  <div class="abs cat-line" style="left:578px"></div>
  <div class="abs cat-line" style="left:970px"></div>
</section>

<section class="section featured-products">
  <h2 class="abs sec-title" style="top:55px">FEATURED PRODUCTS</h2>
  <div class="abs rule" style="left:579px;top:122px;width:40px"></div>

  <div class="abs product" style="left:26px">
    <div class="thumb" role="img" aria-label="Fashion magazine layout mockup" style="background:linear-gradient(135deg,#d9c9c5,#8f7470)"></div>
    <div class="cart-dot"></div>
    <h4>Sed ut perspiciatis unde omnis iste natus error sit volupta</h4>
    <p>Lorem ipsum dolor sit amet, cons ectetur adipiscing eli, sed.</p>
    <div class="price">$59.00</div>
    <div class="btn">Shop Now</div>
  </div>
  <div class="abs product" style="left:318px">
    <div class="thumb" role="img" aria-label="Software box mockup" style="background:linear-gradient(135deg,#e6eaee,#1c2345 60%,#c9cfd6)"></div>
    <div class="cart-dot"></div>
    <h4>Sed ut perspiciatis unde omnis iste natus error sit volupta</h4>
    <p>Lorem ipsum dolor sit amet, cons ectetur adipiscing eli, sed.</p>
    <div class="price">$59.00</div>
    <div class="btn">Shop Now</div>
  </div>
  <div class="abs product" style="left:610px">
    <div class="thumb" role="img" aria-label="Editorial layouts on laptop, tablet and phone" style="background:linear-gradient(135deg,#5a5a5e,#2c2c30)"></div>
    <div class="cart-dot"></div>
    <h4>Sed ut perspiciatis unde omnis iste natus error sit volupta</h4>
    <p>Lorem ipsum dolor sit amet, cons ectetur adipiscing eli, sed.</p>
    <div class="price">$59.00</div>
    <div class="btn">Shop Now</div>
  </div>
  <div class="abs product" style="left:904px">
    <div class="thumb" role="img" aria-label="Product box package mockup in dark red tones" style="background:linear-gradient(135deg,#3a4160,#7a2a22 60%,#2a2f48)"></div>
    <div class="cart-dot"></div>
    <h4>Sed ut perspiciatis unde omnis iste natus error sit volupta</h4>
    <p>Lorem ipsum dolor sit amet, cons ectetur adipiscing eli, sed.</p>
    <div class="price">$59.00</div>
    <div class="btn">Shop Now</div>
  </div>

  <div class="abs pager">
    <svg width="12" height="14" viewBox="0 0 12 14" fill="none" stroke="#1c2152" stroke-width="2"><path d="M9 1L3 7l6 6"/></svg>
    <i class="on"></i><i></i><i></i><i></i><i></i><i></i>
    <svg width="12" height="14" viewBox="0 0 12 14" fill="none" stroke="#1c2152" stroke-width="2"><path d="M3 1l6 6-6 6"/></svg>
  </div>
</section>

<footer class="section footer">
  <div class="abs logo" style="left:149px;top:50px">Pelix Bridge</div>
  <div class="abs" style="left:231px;top:117px;font-size:13px">FOLLOW US</div>
  <div class="abs social" style="left:160px;top:153px"><span>Circlo</span><span>Tunely</span><span>Snapra</span><span>Postr</span><span>Linkwork</span></div>

  <h5 class="abs" style="left:466px;top:50px">MENU</h5>
  <ul class="abs" style="left:466px;top:79px"><li>Home</li><li>Services</li><li>Marketplace</li><li>About Us</li><li>Contact</li></ul>

  <h5 class="abs" style="left:605px;top:50px">LOCATIONS</h5>
  <ul class="abs" style="left:608px;top:79px"><li>Kisima Rd</li><li>Riverside</li><li>Nairobi Kenya</li></ul>

  <h5 class="abs" style="left:790px;top:50px">NEWSLETTER SUBSCRIBE</h5>
  <div class="abs field">
    <svg width="15" height="11" viewBox="0 0 15 11"><rect width="15" height="11" rx="1" fill="#1c2152"/><path d="M1 1l6.5 5L14 1" stroke="#fff" stroke-width="1.3" fill="none"/></svg>
    Email id
  </div>
  <div class="abs subscribe">SUBSCRIBE</div>

  <div class="abs divider"></div>
  <div class="abs pay"><span style="font-size:17px">PayLoop</span><span class="chip">Orbica</span><span class="chip">Vexa</span><span class="chip">Amerigo</span><span class="chip">Mobipesa</span></div>
  <div class="abs copyright">Copyright © 2024 All Rights Reserved</div>
</footer>

</body>
</html>
```